Single Page Brochure for Infertile Couples

We are a surrogacy firm that matches infertile couples with gestational surrogates who will help them achieve their goals of parenthood. We are looking for a brochure designed to introduce our services, but to also drive them to our website for more info or contact us directly. We envision a single page "slim jim" type brochure that coordinates in color and theme with our website for continuity of design. Our website is www.brightwillowsurrogacy.com.

Target Market(s)

Couples age 25-50 with no children or difficulty having a child, have been through infertility treatments, typically higher income earners

Industry/Entity Type

Medical

Requirements
Nice to have
• Designs that coordinate with the website (www.brightwillowsurrogacy.com), very clean, driving clients to the website or to contact us.

```html
<!DOCTYPE html>
<html lang="en">
<head>
<meta charset="utf-8">
<title>The Path to Parenthood – Bright Willow Surrogacy</title>
<link href="https://fonts.googleapis.com/css2?family=Arimo:wght@400;700&family=Parisienne&display=swap" rel="stylesheet">
<style>
  :root {
    --purple: #9a4f98;
    --purple-text: #8c3f8a;
    --green: #a9c56c;
    --white: #ffffff;
  }
  html, body {
    margin: 0;
    padding: 0;
    width: 1200px;
    height: 2676px;
    overflow: hidden;
    background: var(--white);
  }
  .brochure {
    position: relative;
    width: 1200px;
    height: 2676px;
    overflow: hidden;
    background: var(--white);
    font-family: "Arimo", Arial, sans-serif;
  }
  .artwork {
    position: absolute;
    inset: 0;
  }
  .title-band {
    position: absolute;
    left: 0;
    top: 1328px;
    width: 1200px;
    height: 134px;
    background: var(--green);
    display: flex;
    align-items: center;
  }
  .title-band__heading {
    margin: 0 0 0 20px;
    font-family: "Parisienne", cursive;
    font-weight: 400;
    font-size: 100px;
    line-height: 1;
    color: var(--white);
    white-space: nowrap;
  }
  .intro {
    position: absolute;
    left: 472px;
    top: 1500px;
    width: 650px;
    color: var(--purple-text);
    font-size: 40px;
    line-height: 47px;
  }
  .intro p {
    margin: 0 0 47px;
  }
  .footer-band {
    position: absolute;
    left: 0;
    top: 2488px;
    width: 1200px;
    height: 188px;
    background: var(--green);
    color: var(--white);
    text-align: center;
  }
  .footer-band__url {
    margin: 14px 0 0;
    font-size: 78px;
    line-height: 100px;
    white-space: nowrap;
  }
  .footer-band__cities {
    margin: 8px 0 0;
    font-size: 28px;
    font-weight: 700;
    letter-spacing: 3px;
  }
</style>
</head>
<body>
<div class="brochure">
  <svg class="artwork" width="1200" height="2676" viewBox="0 0 1200 2676" xmlns="http://www.w3.org/2000/svg">
    <defs>
      <linearGradient id="skinTone" x1="0" y1="0" x2="1" y2="1">
        <stop offset="0" stop-color="#f6e6dc"/>
        <stop offset="1" stop-color="#e3b9a0"/>
      </linearGradient>
      <linearGradient id="familyTone" x1="0" y1="0" x2="1" y2="1">
        <stop offset="0" stop-color="#5a4a44"/>
        <stop offset="1" stop-color="#e9c9b6"/>
      </linearGradient>
      <radialGradient id="hopeTone" cx="0.5" cy="0.5" r="0.6">
        <stop offset="0" stop-color="#e2b868"/>
        <stop offset="1" stop-color="#8a5a22"/>
      </radialGradient>
      <linearGradient id="kissTone" x1="0" y1="0" x2="1" y2="0">
        <stop offset="0" stop-color="#c8957c"/>
        <stop offset="0.5" stop-color="#f3ddd0"/>
        <stop offset="1" stop-color="#b98a74"/>
      </linearGradient>
      <linearGradient id="handTone" x1="0" y1="0" x2="1" y2="1">
        <stop offset="0" stop-color="#efd4c4"/>
        <stop offset="1" stop-color="#fbeee6"/>
      </linearGradient>
    </defs>

    <g class="photo photo--family" role="img" aria-label="Photo of parents smiling with their baby">
      <rect x="0" y="0" width="560" height="462" fill="url(#familyTone)"/>
    </g>
    <g class="photo photo--hope" role="img" aria-label="Photo of cupped hands holding an egg marked HOPE">
      <rect x="0" y="476" width="520" height="462" fill="url(#hopeTone)"/>
    </g>
    <g class="photo photo--kiss" role="img" aria-label="Photo of parents kissing a laughing baby">
      <rect x="0" y="952" width="640" height="376" fill="url(#kissTone)"/>
    </g>

    <g class="photo photo--twins" role="img" aria-label="Photo of two newborn babies lying side by side">
      <path d="M540,0 H1200 V1328 H700 Q372,690 540,0 Z" fill="url(#skinTone)"/>
    </g>
    <path class="curve-gap" d="M510,-10 Q326,690 672,1340" fill="none" stroke="var(--white)" stroke-width="14"/>
    <path class="curve curve--top" d="M534,-10 Q352,690 700,1340" fill="none" stroke="var(--purple)" stroke-width="26"/>

    <g class="photo photo--hand" role="img" aria-label="Photo of a tiny baby hand">
      <path d="M0,1462 H110 C430,1640 520,2120 250,2488 H0 Z" fill="url(#handTone)"/>
    </g>
    <path class="curve curve--bottom" d="M110,1462 C430,1640 520,2120 250,2488" fill="none" stroke="var(--purple)" stroke-width="24"/>
  </svg>

  <div class="title-band">
    <h1 class="title-band__heading">The Path to Parenthood</h1>
  </div>

  <div class="intro">
    <p>The path to parenthood can be a difficult one - where to start, what decisions to make, how far to go. No one path is the same, and everyone's journey is different. Let Bright Willow Surrogacy be your guide. The caring nature and concierge approach of our practice allows us to foster personalized care in an intimate environment.</p>
    <p>The infertility expertise of our group is unsurpassed. At Bright Willow Surrogacy, we will work closely with you, providing a tailored approach to your family building objectives, with the ultimate goal of being part of your miracle. Let us be your guide on this - the road less traveled.</p>
  </div>

  <footer class="footer-band">
    <p class="footer-band__url">www.brightwillowsurrogacy.com</p>
    <p class="footer-band__cities">LAKEMONT / BRIARWOOD / SILVER HILLS / SUNHAVEN</p>
  </footer>
</div>
</body>
</html>
```